Need business card designed for a Mobile RV Repair business

I need a business card designed

Welding sparks

Industry/Entity Type

Rv Repair , Mobile Welding & Fabrication

Contact Information for Business Card

****

Colors
0054AA
0677BA
7BADD7
CADEEF
E8F1F8

Requirements
Nice to have
• welding sparks, list of services, welding vector

```html
<!DOCTYPE html>
<html lang="en">
<head>
<meta charset="utf-8">
<title>R&amp;T Mobile RV &amp; Coach Repair – Business Card</title>
<link href="https://fonts.googleapis.com/css2?family=Montserrat:wght@400;500;600&display=swap" rel="stylesheet">
<style>
  :root {
    --backdrop: #2a2a2a;
    --card: #ffffff;
    --card-shade: #ececec;
    --teal: #0f9a8e;
    --ink: #3a3a3a;
    --orange: #f08a1c;
    --yellow: #f6d53a;
  }
  * { box-sizing: border-box; margin: 0; padding: 0; }
  html, body { width: 1200px; height: 900px; overflow: hidden; }
  body {
    background: var(--backdrop);
    font-family: "Montserrat", Arial, sans-serif;
    display: flex; flex-direction: column; align-items: center; justify-content: center;
    gap: 24px;
  }
  .card {
    width: 700px; height: 400px;
    background: linear-gradient(135deg, var(--card-shade) 0%, var(--card) 55%);
    border-radius: 34px;
    position: relative;
    box-shadow: 0 10px 24px rgba(0,0,0,.45);
  }
  .brand {
    position: absolute; left: 50px; top: 170px;
    display: flex; align-items: center; gap: 12px;
    color: var(--teal); font-weight: 500; font-size: 19px; line-height: 1.25;
    width: 280px;
  }
  .brand-dot { width: 16px; height: 16px; border-radius: 50%; background: var(--teal); flex: none; }
  .rule {
    height: 2px; background: linear-gradient(90deg, var(--orange), var(--yellow) 60%, transparent);
  }
  /* back: services */
  .services { position: absolute; left: 360px; top: 70px; width: 310px; }
  .services-title { color: var(--teal); font-size: 22px; font-weight: 500; margin-bottom: 6px; }
  .services .rule { margin-bottom: 14px; }
  .service-list { list-style: none; }
  .service-list li {
    color: var(--ink); font-size: 15px; line-height: 28px;
    display: flex; align-items: center; gap: 10px;
  }
  .service-list li::before {
    content: ""; width: 10px; height: 10px; border-radius: 50%; background: var(--teal); flex: none;
  }
  /* front: contact */
  .contact { position: absolute; left: 380px; top: 200px; width: 290px; }
  .contact-name { color: var(--teal); font-size: 22px; font-weight: 600; letter-spacing: .5px; }
  .contact-role { color: var(--ink); font-size: 17px; margin: 2px 0 8px; }
  .contact .rule { margin-bottom: 12px; }
  .contact-line { display: flex; align-items: center; gap: 10px; color: var(--ink); font-size: 15px; line-height: 28px; }
  .contact-line svg { width: 16px; height: 16px; fill: var(--teal); flex: none; }
</style>
</head>
<body>
  <section class="card card-back">
    <div class="brand"><span class="brand-dot"></span><span>R&amp;T Mobile RV &amp; Coach Repair</span></div>
    <div class="services">
      <h2 class="services-title">Our Services</h2>
      <div class="rule"></div>
      <ul class="service-list">
        <li>RV Repair</li>
        <li>Electrical</li>
        <li>Plumbing</li>
        <li>Mobile Welding</li>
        <li>General repairs &amp; modifications</li>
        <li>Custom fabrication</li>
        <li>Gates/Fences</li>
        <li>Aluminum welding</li>
      </ul>
    </div>
  </section>

  <section class="card card-front">
    <div class="brand"><span class="brand-dot"></span><span>R&amp;T Mobile RV &amp; Coach Repair</span></div>
    <div class="contact">
      <h1 class="contact-name">MARCO ELLISON</h1>
      <p class="contact-role">Owner</p>
      <div class="rule"></div>
      <p class="contact-line">
        <svg viewBox="0 0 24 24" aria-hidden="true"><path d="M6.6 10.8a15.1 15.1 0 0 0 6.6 6.6l2.2-2.2a1 1 0 0 1 1-.25 11.4 11.4 0 0 0 3.6.57 1 1 0 0 1 1 1V20a1 1 0 0 1-1 1A17 17 0 0 1 3 4a1 1 0 0 1 1-1h3.5a1 1 0 0 1 1 1c0 1.25.2 2.45.57 3.6a1 1 0 0 1-.25 1z"/></svg>
        555.014.2290
      </p>
      <p class="contact-line">
        <svg viewBox="0 0 24 24" aria-hidden="true"><path d="M2 5h20v14H2zm2 2v.5l8 5 8-5V7l-8 5z"/></svg>
        rtmobilecoach@example.com
      </p>
    </div>
  </section>
</body>
</html>
```